Australian Skilled Migration

We need to design a add/flyer for a newspaper/magazine to promote our Australian Migration firm services. We targeting overseas graduating students and professionals who would like to Permanently Migrate to Australia.

We would like to advertise following services to our potential clients:

AUSTRALIA NEEDS YOU!!!

# Are you young and energetic individual?
# Do you have qualifications, work experiences or both?
# Perhaps you would like to open a small business, and sponsor yourself to live in Australia?
# Aspiring for job security and the highest living standards?

Contact us to find out how we can help you with Permanent Migration to Australia.

First consultation and eligibility assessment is free ! Tell your friends about us and receive a discount on your future fees!!

For more information please visit our website: www.corvintrak.org.au

(for a background we would like to use Australian themes such as: sandy beaches, ect... light colours)

Target Market(s)

Students
University graduates
Trade people with qualifications
Industry professionals
Anyone who wants to migrate to Australia

Industry/Entity Type

Security

Requirements
Must have
• our logo and website
easy to see and read the txt

Catchy Background
Nice to have
• as per our requirements
(designer questions, please e-mail: info@corvintrak.org. au)

```html
<!DOCTYPE html>
<html lang="en">
<head>
<meta charset="utf-8">
<title>Harlow &amp; Co – Australian Skilled Migration</title>
<link rel="stylesheet" href="https://fonts.googleapis.com/css2?family=Arimo:ital,wght@0,700;1,700&family=Roboto+Condensed:ital,wght@0,700;1,700;1,900&display=swap">
<style>
  :root {
    --sand: #e8dcb6;
    --red: #c8101a;
    --deep-red: #8a1414;
    --ink-blue: #27199a;
    --navy: #1f2f5e;
    --white: #ffffff;
    --black: #111111;
  }
  html, body {
    margin: 0;
    padding: 0;
    overflow: hidden;
    background: var(--sand);
  }
  p, h1, ul { margin: 0; }
  .flyer {
    position: relative;
    width: 849px;
    height: 1200px;
    overflow: hidden;
    background: var(--sand);
    font-family: "Arimo", Arial, sans-serif;
  }
  .headline {
    position: absolute;
    top: 24px;
    left: 0;
    width: 100%;
    text-align: center;
    font-family: "Roboto Condensed", "Arial Narrow", sans-serif;
    font-style: italic;
    font-weight: 700;
    font-size: 55px;
    line-height: 1.1;
    color: var(--red);
    letter-spacing: -0.3px;
  }
  .headline .soft { font-size: 50px; }
  .criteria {
    position: absolute;
    top: 97px;
    left: 62px;
    padding: 0;
    list-style: none;
    color: var(--ink-blue);
    font-weight: 700;
    font-size: 26px;
    line-height: 1.4;
  }
  .criteria li {
    position: relative;
    padding-left: 30px;
    margin-bottom: 1px;
  }
  .criteria li::before {
    content: "★";
    position: absolute;
    left: 0;
    top: 0;
    color: var(--red);
    font-size: 22px;
  }
  .criteria .indent { padding-left: 8px; }
  .brand {
    position: absolute;
    top: 302px;
    left: 150px;
    display: flex;
    align-items: center;
    gap: 22px;
  }
  .brand-dot {
    width: 190px;
    height: 150px;
    border-radius: 50%;
    border: 2px solid var(--red);
    box-sizing: border-box;
  }
  .brand-name {
    font-size: 50px;
    font-weight: 700;
    color: var(--red);
    line-height: 1;
  }
  .brand-tag {
    margin-top: 8px;
    font-size: 19px;
    font-weight: 700;
    color: var(--red);
  }
  .offer {
    position: absolute;
    top: 466px;
    left: 0;
    width: 100%;
    text-align: center;
    font-family: "Roboto Condensed", "Arial Narrow", sans-serif;
    font-style: italic;
    font-weight: 900;
    font-size: 37px;
    line-height: 1.15;
    color: var(--ink-blue);
    letter-spacing: 1.5px;
    z-index: 2;
  }
  .offer .free { color: var(--deep-red); }
  .photo {
    position: absolute;
    top: 555px;
    left: 0;
    width: 849px;
    height: 530px;
    background:
      radial-gradient(ellipse 55% 60% at 50% 55%, rgba(214,150,120,0.85), rgba(214,150,120,0) 70%),
      radial-gradient(ellipse 30% 45% at 15% 70%, rgba(225,190,110,0.8), rgba(225,190,110,0) 70%),
      radial-gradient(ellipse 30% 45% at 85% 65%, rgba(200,110,70,0.75), rgba(200,110,70,0) 70%),
      linear-gradient(180deg, rgba(232,220,182,0) 0%, rgba(120,110,100,0.35) 60%, rgba(150,60,100,0.4) 100%);
    z-index: 1;
  }
  .contact-call {
    position: absolute;
    top: 568px;
    left: 0;
    width: 100%;
    text-align: center;
    font-family: "Roboto Condensed", "Arial Narrow", sans-serif;
    font-weight: 700;
    font-size: 36px;
    line-height: 1.17;
    color: var(--red);
    letter-spacing: 1.2px;
    z-index: 2;
  }
  .referral {
    position: absolute;
    top: 992px;
    left: 0;
    width: 100%;
    text-align: center;
    font-family: "Roboto Condensed", "Arial Narrow", sans-serif;
    font-style: italic;
    font-weight: 700;
    font-size: 36px;
    line-height: 1.08;
    color: var(--red);
    letter-spacing: 1.5px;
    z-index: 2;
  }
  .more {
    position: absolute;
    top: 1094px;
    left: 0;
    width: 100%;
    text-align: center;
    font-style: italic;
    font-weight: 700;
    font-size: 24px;
    line-height: 1.2;
    color: var(--black);
  }
  .web-band {
    position: absolute;
    left: 0;
    bottom: 0;
    width: 100%;
    height: 72px;
    background: var(--navy);
    display: flex;
    align-items: center;
    justify-content: center;
    color: var(--white);
    font-weight: 700;
    font-size: 38px;
    letter-spacing: 8px;
  }
</style>
</head>
<body>
<main class="flyer">
  <h1 class="headline">AUSTRALIA NEEDS YOU <span class="soft">if you are</span></h1>

  <ul class="criteria">
    <li>Young and energetic individual</li>
    <li>Is qualified and has work experiences</li>
    <li>Interested to open a small business and sponsor<br><span class="indent">yourself to live in Australia</span></li>
    <li>Aspiring for job security and highest living standards</li>
  </ul>

  <div class="brand">
    <div class="brand-dot"></div>
    <div>
      <div class="brand-name">Harlow &amp; Co</div>
      <div class="brand-tag">Lawyers &amp; Migration Agents</div>
    </div>
  </div>

  <p class="offer">FIRSTCONSULTATION AND<br>ELIGIBILITY ASSESSMENT IS <span class="free">FREE</span></p>

  <div class="photo" role="img" aria-label="Photo of three smiling young people giving a thumbs up"></div>

  <p class="contact-call">Contact Us And Find Out How We Can Help<br>You With Permanent Migration to Australia</p>

  <p class="referral">Tell Your Friends About Us And Get A Discount<br>On your Future Fees!</p>

  <p class="more">Visit our website and know more about &nbsp;our other &nbsp;visa services</p>

  <div class="web-band">WWW.CORVINTRAK.ORG.AU</div>
</main>
</body>
</html>
```